Breast Cancer Month Banner

I need a standing banner and a n outdoor banner design
Please include the logos of the sponsors at the bottom or the top
I've include the logos in one file called Back Design and Orchard Lane Logo
12Ft x 3Ft - horizontal banner - This can be a regular banner depicting Breast cancer awareness month #Pinktober. some examples have been attached
2.5Ft x 6Ft - Standing banner - THis banner should be an Infographic type banner depicting breast cancer causes, risk factors and prevention. examples of info graphic have been attached
Health/Medical

```html
<!DOCTYPE html>
<html lang="en">
<head>
<meta charset="utf-8">
<title>Breast Cancer Awareness Month Banners</title>
<link href="https://fonts.googleapis.com/css2?family=Bebas+Neue&display=swap" rel="stylesheet">
<style>
:root{
  --hot-pink:#f73d93;
  --soft-pink:#fe92c8;
  --ribbon-pink:#fd9ccb;
  --white:#ffffff;
  --page:#ffffff;
}
*{margin:0;padding:0;box-sizing:border-box}
html,body{width:1200px;height:774px;overflow:hidden;background:var(--page)}
body{position:relative;font-family:"Bebas Neue",sans-serif;color:var(--hot-pink);line-height:1}
.abs{position:absolute}
.standee{left:50px;top:42px;width:286px;height:664px;background:var(--white);box-shadow:0 0 6px rgba(0,0,0,.12)}
.outdoor{left:406px;top:323px;width:754px;height:277px;background:var(--white);box-shadow:0 0 8px rgba(0,0,0,.25)}
.lockup{left:1025px;top:0;width:140px;height:270px}
.flag{position:absolute;left:0;top:0}
.flag-text{position:absolute;color:var(--white);text-align:center;width:100%}
.ribbon{position:absolute;background:var(--ribbon-pink);border-radius:40% 40% 10% 10%}
.awareness{position:absolute;color:var(--hot-pink);text-align:center}
.headline{position:absolute}
.body-copy{position:absolute;color:var(--soft-pink)}
.body-copy strong{color:var(--hot-pink);font-weight:400}
.band{position:absolute;left:0;width:100%}
.band-light{background:var(--soft-pink)}
.band-hot{background:var(--hot-pink)}
.divider{position:absolute;left:0;width:100%;height:2px;background:var(--white)}
.band-text{position:absolute;left:0;width:100%;text-align:center;color:var(--white)}
.row-icon{position:absolute;width:18px;height:36px;background:var(--white);border-radius:40% 40% 10% 10%}
.center-line{position:absolute;left:0;width:100%;text-align:center}
.client{position:absolute;display:flex;flex-direction:column;align-items:center;justify-content:center;text-align:center;color:var(--hot-pink)}
.client-disc{border-radius:50%;border:3px solid var(--hot-pink);background:var(--ribbon-pink)}
.sponsors{position:absolute;display:grid;grid-template-columns:repeat(3,1fr);align-items:center;justify-items:center;color:var(--hot-pink);text-align:center}
.sponsor{font-size:11px;line-height:1}
</style>
</head>
<body>

<!-- Standing banner -->
<section class="abs standee" aria-label="Standing banner">
  <h1 class="headline" style="left:20px;top:20px;font-size:63px;line-height:53px">BE<br>AWARE!</h1>
  <p class="body-copy" style="left:20px;top:128px;font-size:18.5px;line-height:17px">YOU HAVE A GOOD CHANCE<br>TO <strong>CURE BREAST CANCER</strong><br>BUT <strong>TO TREAT IT</strong> YOU NEED<br>TO <strong>FIND IT!</strong></p>

  <svg class="flag" style="left:184px" width="76" height="100" viewBox="0 0 76 100" aria-hidden="true">
    <path d="M0 0H76V99C62 82 40 80 22 90C14 94 6 96 0 96Z" fill="var(--hot-pink)"/>
  </svg>
  <p class="flag-text" style="left:184px;top:14px;width:76px;font-size:22px;line-height:21px">JOIN US<br>IN THE<br>FIGHT</p>
  <div class="ribbon" role="img" aria-label="Pink awareness ribbon" style="left:232px;top:100px;width:26px;height:40px"></div>
  <p class="awareness" style="left:184px;top:119px;width:64px;font-size:15px;line-height:14px;text-align:left">BREAST<br>CANCER<br>AWARENESS</p>

  <div class="band band-light" style="top:208px;height:170px"></div>
  <p class="band-text" style="top:224px;font-size:30px">THE 10 YEAR SURVIVAL RATE</p>
  <div class="divider" style="top:257px"></div>
  <div class="row-icon" role="img" aria-label="Awareness ribbon icon" style="left:20px;top:270px"></div>
  <p class="band-text" style="left:50px;width:230px;top:266px;font-size:25px;line-height:26px">95% IF CANCER IS DETECTED<br>BY A MAMMOGRAM</p>
  <div class="divider" style="top:317px"></div>
  <div class="row-icon" role="img" aria-label="Awareness ribbon icon" style="left:20px;top:326px"></div>
  <p class="band-text" style="left:50px;width:230px;top:322px;font-size:25px;line-height:27px">85% IF A LUMP IS THE FIRST<br>SIGN IDENTIFIED</p>

  <p class="center-line" style="top:389px;font-size:24px">1 IN 8 WILL DEVELOP BREAST CANCER</p>
  <div class="band band-hot" style="top:419px;height:66px"></div>
  <p class="band-text" style="top:425px;font-size:26px;line-height:26px">IF YOU THINK SOMETHING IS<br>WRONG, SEEK HELP IMMEDIATELY</p>
  <p class="center-line" style="top:500px;font-size:30px">#BREAST AWARENESS MONTH</p>

  <div class="client" style="left:10px;top:538px;width:108px;height:108px">
    <div class="client-disc" style="width:18px;height:18px;margin-bottom:4px"></div>
    <span style="font-size:13px;line-height:13px">HOPE CIRCLE<br>SKN INC</span>
  </div>
  <div class="sponsors" style="left:124px;top:544px;width:160px;height:100px;grid-template-rows:repeat(3,1fr)">
    <span class="sponsor">SOLANO<br>PHARMACY</span>
    <span class="sponsor">CLEARBROOK</span>
    <span class="sponsor">ORCHARD<br>LANE</span>
    <span class="sponsor">PALMERA<br>APPAREL</span>
    <span class="sponsor" style="grid-column:span 2">RIDGEVIEW SPRINGS<br>VITACARE MEDICAL</span>
    <span class="sponsor" style="grid-column:span 2">WELLSPRING PHARMACY</span>
    <span class="sponsor">TIDEWATER BAR</span>
  </div>
</section>

<!-- Outdoor banner -->
<section class="abs outdoor" aria-label="Outdoor banner">
  <svg class="flag" style="left:22px" width="132" height="168" viewBox="0 0 132 168" aria-hidden="true">
    <path d="M0 0H132V165C108 140 72 138 42 152C26 160 12 167 0 166Z" fill="var(--hot-pink)"/>
  </svg>
  <p class="flag-text" style="left:22px;top:16px;width:132px;font-size:44px;line-height:36px">JOIN US<br>IN THE<br><span style="font-size:52px">FIGHT</span></p>
  <div class="ribbon" role="img" aria-label="Pink awareness ribbon" style="left:104px;top:156px;width:48px;height:68px"></div>
  <p class="awareness" style="left:22px;top:189px;width:112px;font-size:26px;line-height:24px">BREAST<br>CANCER<br>AWARENESS</p>

  <h1 class="headline" style="left:175px;top:18px;font-size:90px;white-space:nowrap">BE AWARE!</h1>
  <p class="body-copy" style="left:176px;top:106px;font-size:27px;line-height:25px">YOU HAVE A GOOD CHANCE TO <strong>CURE BREAST CANCER</strong><br>BUT <strong>TO TREAT IT</strong> YOU NEED TO <strong>FIND IT!</strong></p>
  <p class="headline" style="left:176px;top:193px;font-size:18px">IF YOU THINK SOMETHING IS WRONG, SEEK HELP IMMEDIATELY</p>
  <p class="headline" style="left:176px;top:216px;font-size:45px;white-space:nowrap">#BREAST AWARENESS MONTH</p>

  <div class="client" style="left:590px;top:12px;width:148px;height:148px">
    <div class="client-disc" style="width:26px;height:26px;margin-bottom:6px"></div>
    <span style="font-size:17px;line-height:16px">HOPE CIRCLE<br>SKN INC</span>
  </div>
  <div class="sponsors" style="left:590px;top:170px;width:156px;height:98px;grid-template-rows:repeat(3,1fr)">
    <span class="sponsor">SOLANO<br>PHARMACY</span>
    <span class="sponsor">CLEARBROOK</span>
    <span class="sponsor">ORCHARD<br>LANE</span>
    <span class="sponsor">PALMERA<br>APPAREL</span>
    <span class="sponsor" style="grid-column:span 2">RIDGEVIEW SPRINGS<br>VITACARE MEDICAL</span>
    <span class="sponsor" style="grid-column:span 2">WELLSPRING PHARMACY</span>
    <span class="sponsor" style="white-space:nowrap">TIDEWATER BAR</span>
  </div>
</section>

<!-- Campaign lockup -->
<section class="abs lockup" aria-label="Join us in the fight lockup">
  <svg class="flag" width="131" height="164" viewBox="0 0 131 164" aria-hidden="true">
    <path d="M0 0H131V160C108 138 72 136 42 150C26 157 12 163 0 162Z" fill="var(--hot-pink)"/>
  </svg>
  <p class="flag-text" style="top:13px;width:131px;font-size:42px;line-height:37px">JOIN US<br>IN THE<br><span style="font-size:48px">FIGHT</span></p>
  <div class="ribbon" role="img" aria-label="Pink awareness ribbon" style="left:84px;top:162px;width:50px;height:70px"></div>
  <p class="awareness" style="left:0;top:194px;width:108px;font-size:26px;line-height:24px">BREAST<br>CANCER<br>AWARENESS</p>
</section>

</body>
</html>
```